ROVA.GYM Health & Fitness Online - Around me page

I need the design of an "around me" page for a mobile app. This page when opening should display a map, with identified points on the map and a list of the items seen on the map. All the subscreens also need to be designed and should include the following.
The "Around me" page is a mobile app screen that displays
- Health and fitness facilities around me on a map and on a list, these can include:
- Fitness Centers, Hotels that have Gyms, Fitness Studios, Wellness & SPA, Group fitness classes
The user also has the possibility to add a new location
The user has the possibility to search in general or use filters on the search, these filters include
- What are you looking for?
- Fitness Facility
- Functional area, free weights, cardio machines, workout machines
- Wellness
- Swimming pool, Sauna, Hamam, Massage
- Group classes
- Search by fitness program, fitness type, fitness Brand
- Professional
- Personal trainer, nutritionist, Physiotherapist, Fitness Instructor, Coach
When the user selects one item on the map, the selected entry on the list gets selected, depending on the item type some info is shown, by selecting the item on the list a detail page is displayed, with all the information of the item.
For example, if it's a fitness, it should show a profile picture, a logo, the address, contact information, the opening hours, the possibility to buy the access to the fitness. The size of the fitness, the capabilities of the fitness (free weight, cardio, sauna etc etc)
If it's a hotel, the same type of info like for the gym should display, just it needs to be clear it is a hotel with a fitness, what's important are the facilities and it's contents. Again The user can book this facility.
Upon booking the facility the user gets to see a QR code, this QR code will be scanned at the entrance.
If the item is a group fitness class, it can be delivered at a gym or studio, capacity info is required, the instructor that is presenting the class, the day and time of the class, and a button to book the class.
The item can also be a professional, in this case, his profile picture is shown, with his name and country, the languages he speaks, the programs he's certified on, his bio and experience, where he works, and the services he delivers, there is also a book this professional button, where the user can send a message to the professional.
Please make these screens modern, functional, simple, UX easy and intuitive experience for the user.
Please use the color-coding of the template I will send you, this template is not well designed, so please propose something 1000x better.
Target Market(s)
Users of this page are prople that are looking for a place to do fitness.
Industry/Entity Type
Health and Fitness
- I use Sketch for my design, if you can make it or in a format where I can import it to sketch it would help.

```html
<!DOCTYPE html>
<html lang="en">
<head>
<meta charset="utf-8">
<title>Around Me</title>
<link rel="stylesheet" href="https://fonts.googleapis.com/css2?family=Lato:wght@400;700;900&display=swap">
<style>
  :root {
    --crimson: #d81b4f;
    --crimson-deep: #c8163f;
    --coral: #f58b86;
    --coral-soft: #fbb3a8;
    --ink: #161616;
    --navy: #21232f;
    --white: #ffffff;
    --chip-border: #d6d6d6;
    --map-light: #ececec;
    --map-mid: #dcdcdc;
    --divider: #3a3d4a;
    --icon-dark: #2a2a2a;
    --ring-grey: #e3e3e3;
  }
  * { box-sizing: border-box; margin: 0; padding: 0; }
  html, body {
    width: 1200px; height: 3848px; overflow: hidden;
    background: var(--white);
    font-family: "Lato", Arial, sans-serif;
  }
  .screen {
    position: absolute; left: 0; top: 0;
    width: 450px; height: 1443px;
    transform: scale(2.66667); transform-origin: 0 0;
    background: var(--white); overflow: hidden;
  }
  .abs { position: absolute; }

  /* Header */
  .hero-layer { position: absolute; left: 0; right: 0; border-radius: 0 0 22px 22px; }
  .hero-layer--soft { top: 60px; height: 148px; background: var(--coral-soft); }
  .hero-layer--coral { top: 60px; height: 138px; background: var(--coral); }
  .hero-layer--main { top: 60px; height: 130px; background: linear-gradient(180deg, var(--crimson) 0%, var(--crimson-deep) 100%); }
  .top-bar {
    position: absolute; left: 0; top: 0; width: 450px; height: 86px;
    background: var(--white); border-radius: 0 0 22px 22px;
  }
  .page-title { position: absolute; left: 17px; top: 32px; font-size: 21px; font-weight: 900; color: var(--ink); letter-spacing: -0.2px; }
  .top-icon { position: absolute; top: 32px; width: 30px; height: 26px; }
  .badge {
    position: absolute; top: -9px; right: -9px; width: 19px; height: 19px; border-radius: 50%;
    background: var(--crimson); color: var(--white); font-size: 11px; font-weight: 900;
    display: flex; align-items: center; justify-content: center;
  }

  .search-bar {
    position: absolute; left: 13px; top: 110px; width: 424px; height: 53px;
    background: var(--white); border-radius: 27px;
  }
  .search-bar svg { position: absolute; left: 21px; top: 18px; }
  .search-label { position: absolute; left: 50px; top: 17px; font-size: 16px; font-weight: 700; color: var(--ink); }
  .add-location {
    position: absolute; right: 5px; top: 5px; width: 152px; height: 43px; border-radius: 22px;
    background: var(--ink); color: var(--white); font-size: 16px; font-weight: 700;
    display: flex; align-items: center; justify-content: center;
  }

  /* Filter chips */
  .chip {
    position: absolute; height: 38px; border-radius: 19px; border: 1px solid var(--chip-border);
    background: var(--white); font-size: 14px; font-weight: 700; color: var(--ink);
    display: flex; align-items: center; justify-content: center;
  }
  .chip--active { background: var(--crimson); border-color: var(--crimson); color: var(--white); }

  /* Map */
  .map-area { position: absolute; left: 0; top: 350px; width: 450px; height: 570px; }
  .map-pin-label {
    position: absolute; width: 125px; height: 41px; background: var(--white); border-radius: 8px;
    box-shadow: 0 2px 6px rgba(0,0,0,0.15); text-align: center; padding-top: 3px;
  }
  .map-pin-label::after {
    content: ""; position: absolute; left: 50%; bottom: -7px; margin-left: -7px;
    border-left: 7px solid transparent; border-right: 7px solid transparent; border-top: 7px solid var(--white);
  }
  .pin-name { font-size: 15px; font-weight: 900; color: var(--crimson); line-height: 17px; }
  .pin-street { font-size: 14px; color: var(--ink); line-height: 17px; }
  .map-dot {
    position: absolute; width: 24px; height: 24px; margin: -12px 0 0 -12px; border-radius: 50%;
    background: var(--white); border: 4px solid var(--crimson);
  }

  /* Result list */
  .results {
    position: absolute; left: 0; top: 905px; width: 450px; height: 470px;
    background: var(--navy); border-radius: 24px 24px 0 0;
  }
  .result-row { position: absolute; left: 13px; width: 424px; height: 87px; }
  .result-row + .result-row::before {
    content: ""; position: absolute; left: 0; right: 0; top: 0; height: 1px; background: var(--divider);
  }
  .result-number {
    position: absolute; left: 0; top: 17px; width: 52px; height: 52px; border-radius: 50%;
    background: var(--crimson); color: var(--white); font-size: 18px; font-weight: 900;
    display: flex; align-items: center; justify-content: center;
  }
  .result-title { position: absolute; left: 68px; top: 19px; font-size: 16px; font-weight: 900; color: var(--white); }
  .result-sub { position: absolute; left: 68px; top: 45px; font-size: 15px; color: var(--white); }
  .result-chevron { position: absolute; right: 0; top: 33px; }

  /* Tab bar */
  .tab-bar {
    position: absolute; left: 0; top: 1340px; width: 450px; height: 103px;
    background: var(--white); border-radius: 24px 24px 0 0;
  }
  .tab { position: absolute; display: flex; align-items: center; justify-content: center; }
  .tab--profile { left: 18px; top: 29px; width: 52px; height: 52px; border-radius: 50%; border: 3px solid var(--coral); }
  .tab--profile span { width: 36px; height: 36px; border-radius: 50%; background: var(--white); display: flex; align-items: center; justify-content: center; }
  .tab--center { left: 188px; top: 20px; width: 74px; height: 74px; border-radius: 50%; border: 4px solid var(--ring-grey); background: var(--white); }
</style>
</head>
<body>
<div class="screen">

  <div class="hero-layer hero-layer--soft"></div>
  <div class="hero-layer hero-layer--coral"></div>
  <div class="hero-layer hero-layer--main"></div>

  <header class="top-bar">
    <h1 class="page-title">Around Me</h1>
    <div class="top-icon" style="left:333px;">
      <svg width="30" height="26" viewBox="0 0 30 26" fill="none" stroke="var(--ink)" stroke-width="2.2" stroke-linejoin="round">
        <path d="M4 4h17a3 3 0 0 1 3 3v7a3 3 0 0 1-3 3H10l-5 4v-4H4a3 3 0 0 1-3-3V7a3 3 0 0 1 3-3z"/>
        <path d="M25 9h1a3 3 0 0 1 3 3v6a3 3 0 0 1-3 3h-1v3l-4-3h-6"/>
      </svg>
      <span class="badge">0</span>
    </div>
    <div class="top-icon" style="left:398px;">
      <svg width="26" height="26" viewBox="0 0 26 26" fill="none" stroke="var(--ink)" stroke-width="2.2" stroke-linejoin="round">
        <path d="M13 3a7 7 0 0 1 7 7v6l3 4H3l3-4v-6a7 7 0 0 1 7-7z"/>
        <path d="M10 22a3 3 0 0 0 6 0"/>
      </svg>
      <span class="badge">0</span>
    </div>
  </header>

  <div class="search-bar">
    <svg width="18" height="18" viewBox="0 0 18 18" fill="none" stroke="var(--ink)" stroke-width="2.6" stroke-linecap="round">
      <circle cx="7.5" cy="7.5" r="5.5"/><path d="M12 12l4.5 4.5"/>
    </svg>
    <span class="search-label">Search Adround Me</span>
    <span class="add-location">Add Location</span>
  </div>

  <nav class="filters">
    <span class="chip" style="left:12px;top:234px;width:138px;">Fitness Centers</span>
    <span class="chip chip--active" style="left:169px;top:234px;width:114px;">Hotel Gyms</span>
    <span class="chip" style="left:300px;top:234px;width:137px;">Fitness Studios</span>
    <span class="chip" style="left:90px;top:286px;width:137px;">Wellness &amp; SPA</span>
    <span class="chip" style="left:244px;top:286px;width:117px;">Group Fitness</span>
  </nav>

  <section class="map-area">
    <svg class="abs" width="450" height="570" viewBox="0 0 450 570" role="img" aria-label="Street map of the surrounding neighbourhood with parks, roads and nearby gyms">
      <defs>
        <linearGradient id="mapTone" x1="0" y1="0" x2="0" y2="1">
          <stop offset="0" stop-color="#ececec"/>
          <stop offset="1" stop-color="#dcdcdc"/>
        </linearGradient>
      </defs>
      <path d="M0 50 Q225 -30 450 50 V570 H0 Z" fill="url(#mapTone)"/>
      <circle cx="225" cy="275" r="190" fill="rgba(90,90,90,0.18)" stroke="#d81b4f" stroke-width="1"/>
    </svg>

    <div class="map-pin-label" style="left:55px;top:196px;"><div class="pin-name">Hotel Gyms</div><div class="pin-street">Harbor Ave</div></div>
    <div class="map-dot" style="left:117px;top:269px;"></div>

    <div class="map-pin-label" style="left:292px;top:201px;"><div class="pin-name">Hotel Gyms</div><div class="pin-street">Harbor Ave</div></div>
    <div class="map-dot" style="left:354px;top:274px;"></div>

    <div class="map-pin-label" style="left:158px;top:277px;"><div class="pin-name">Hotel Gyms</div><div class="pin-street">Harbor Ave</div></div>
    <div class="map-dot" style="left:219px;top:350px;"></div>

    <div class="map-pin-label" style="left:311px;top:337px;"><div class="pin-name">Hotel Gyms</div><div class="pin-street">Harbor Ave</div></div>
    <div class="map-dot" style="left:372px;top:410px;"></div>

    <div class="map-pin-label" style="left:164px;top:390px;"><div class="pin-name">Hotel Gyms</div><div class="pin-street">Harbor Ave</div></div>
    <div class="map-dot" style="left:225px;top:463px;"></div>
  </section>

  <section class="results">
    <div class="result-row" style="top:44px;">
      <span class="result-number">1</span>
      <span class="result-title">Hotel Gyms</span>
      <span class="result-sub">Neque porro quisquam</span>
      <svg class="result-chevron" width="12" height="20" viewBox="0 0 12 20" fill="none" stroke="#ffffff" stroke-width="2.2" stroke-linecap="round"><path d="M2 2l8 8-8 8"/></svg>
    </div>
    <div class="result-row" style="top:130px;">
      <span class="result-number">2</span>
      <span class="result-title">Hotel Gyms</span>
      <span class="result-sub">Neque porro quisquam</span>
      <svg class="result-chevron" width="12" height="20" viewBox="0 0 12 20" fill="none" stroke="#ffffff" stroke-width="2.2" stroke-linecap="round"><path d="M2 2l8 8-8 8"/></svg>
    </div>
    <div class="result-row" style="top:217px;">
      <span class="result-number">3</span>
      <span class="result-title">Hotel Gyms</span>
      <span class="result-sub">Neque porro quisquam</span>
      <svg class="result-chevron" width="12" height="20" viewBox="0 0 12 20" fill="none" stroke="#ffffff" stroke-width="2.2" stroke-linecap="round"><path d="M2 2l8 8-8 8"/></svg>
    </div>
    <div class="result-row" style="top:304px;">
      <span class="result-number">4</span>
      <span class="result-title">Hotel Gyms</span>
      <span class="result-sub">Neque porro quisquam</span>
      <svg class="result-chevron" width="12" height="20" viewBox="0 0 12 20" fill="none" stroke="#ffffff" stroke-width="2.2" stroke-linecap="round"><path d="M2 2l8 8-8 8"/></svg>
    </div>
  </section>

  <footer class="tab-bar">
    <div class="tab tab--profile">
      <span>
        <svg width="18" height="18" viewBox="0 0 18 18" fill="#161616"><circle cx="9" cy="5" r="4"/><path d="M1 17a8 6 0 0 1 16 0z"/></svg>
      </span>
    </div>
    <div class="tab" style="left:112px;top:44px;width:36px;height:22px;">
      <svg width="36" height="22" viewBox="0 0 36 22" fill="#2a2a2a">
        <circle cx="18" cy="5" r="4.5"/><circle cx="8" cy="7" r="3.5"/><circle cx="28" cy="7" r="3.5"/>
        <path d="M10 21a8 7 0 0 1 16 0z"/><path d="M1 20a7 6 0 0 1 10-5 9 8 0 0 0-2 5z"/><path d="M35 20a7 6 0 0 0-10-5 9 8 0 0 1 2 5z"/>
      </svg>
    </div>
    <div class="tab tab--center">
      <svg width="40" height="24" viewBox="0 0 40 24" fill="#d81b4f">
        <rect x="2" y="7" width="5" height="10" rx="1.5"/><rect x="7" y="3" width="6" height="18" rx="1.5"/>
        <rect x="13" y="10" width="14" height="4"/>
        <rect x="27" y="3" width="6" height="18" rx="1.5"/><rect x="33" y="7" width="5" height="10" rx="1.5"/>
      </svg>
    </div>
    <div class="tab" style="left:308px;top:46px;width:30px;height:18px;">
      <svg width="30" height="18" viewBox="0 0 30 18" fill="#2a2a2a"><rect x="0" y="1" width="20" height="16" rx="3"/><path d="M21 7l9-5v14l-9-5z"/></svg>
    </div>
    <div class="tab" style="left:394px;top:44px;width:24px;height:22px;">
      <svg width="24" height="22" viewBox="0 0 24 22" fill="#2a2a2a"><rect y="1" width="24" height="3" rx="1"/><rect y="9.5" width="24" height="3" rx="1"/><rect y="18" width="24" height="3" rx="1"/></svg>
    </div>
  </footer>

</div>
</body>
</html>
```